Einladungskarten für Benefizveranstaltung
Zielgruppe
vorrangig Unternehmer;
Privatpersonen
Sportbegeisterte
Aufgabenstellung
Wir benötigen für eine Veranstaltung mit 3 Terminen an 3 vers. Standorten zwei Einladungskarten.
1.) off. Einladung & 2.) VIP-Einladung
Bei der Veranstaltung handelt es sich um einen Vortrag des blinden Bergsteigers Timo Brandler, der alle Seven Summits (die höchsten Gifpel der Kontinente) erreichen möchte. www.timobrandler-vortrag.com
Die Betriebs-Forum unterstützt ihn dabei und braucht die Hilfe von anderen Unternehmen & Privatpersonen. Diese werden zur Veranstaltung eingeladen.
Das Design der Einladungskarten soll an unser Corporate Design angepasst werden (www.betriebs-forum.eu) aber auch den Aspekt "Bergsteigen, Natur, Timo Brandler" beinhalten.

```html
<!DOCTYPE html>
<html lang="de">
<head>
<meta charset="utf-8">
<title>Balanceakt – Einladung Betriebs-Forum 2011</title>
<link rel="stylesheet" href="https://fonts.googleapis.com/css2?family=Open+Sans:wght@400;600;700&display=swap">
<style>
  :root {
    --orange: #e2661f;
    --blue: #1d5793;
    --blue-deep: #123f73;
    --snow: #e9eef2;
    --grey: #8c8c8c;
    --grey-dark: #5a5a5a;
    --text: #555;
    --line: #c9c9c9;
    --paper: #ffffff;
    --bg: #ececec;
  }
  * { box-sizing: border-box; margin: 0; padding: 0; }
  html, body { width: 1200px; height: 1200px; overflow: hidden; }
  body {
    background: var(--bg);
    font-family: "Open Sans", Arial, sans-serif;
    color: var(--text);
    position: relative;
  }
  .sheet { position: absolute; background: var(--paper); overflow: hidden; }

  /* brand mark: name + plain circle */
  .brand { display: flex; align-items: center; gap: 6px; color: var(--orange); font-weight: 600; white-space: nowrap; }
  .brand .dot { width: 12px; height: 12px; border: 2px solid var(--orange); border-radius: 50%; }

  /* ---------- inner spread ---------- */
  .spread { left: 60px; top: 40px; width: 1080px; height: 560px; }
  .spread .photo-strip { position: absolute; left: 0; top: 0; width: 860px; height: 120px;
    background: linear-gradient(90deg, #7d8a9a 0%, #c64a2e 12%, #9b8d78 30%, #6f6a62 48%, #a8a29a 58%, #2f5f9c 72%, #dbe4ee 100%);
    border-bottom-right-radius: 18px; }
  .spread .strip-rule { position: absolute; left: 0; top: 122px; width: 860px; height: 3px; background: var(--orange); }
  .spread .brand { position: absolute; right: 40px; top: 48px; font-size: 18px; }
  .spread .col-left { position: absolute; left: 34px; top: 138px; width: 470px; }
  .spread .title { font-size: 19px; font-weight: 700; letter-spacing: .5px; color: var(--grey-dark); }
  .spread .title .akt { color: var(--orange); }
  .spread .title small { font-size: 12px; font-weight: 400; color: var(--grey); letter-spacing: 0; margin-left: 4px; }
  .spread .title-rule { height: 1px; background: var(--line); margin: 8px 0 18px; }
  .spread p { font-size: 9.5px; line-height: 1.55; text-align: justify; margin-bottom: 9px; }
  .spread p .lead { color: var(--orange); }
  .spread .summits { list-style: none; font-size: 9.5px; line-height: 1.7; margin-top: 4px; }
  .spread .sponsors { position: absolute; left: 34px; bottom: 26px; width: 1010px; display: flex; justify-content: space-between; align-items: center; }
  .spread .sponsor { display: flex; align-items: center; gap: 8px; font-size: 10px; color: var(--grey-dark); font-weight: 600; }
  .spread .sponsor .mark { width: 26px; height: 26px; background: #8b8b8b; }
  .spread .sponsor .mark.wine { background: #7b2a3a; }
  .spread .sponsor .mark.navy { background: #2a62a8; }
  .spread .col-right { position: absolute; left: 540px; top: 125px; width: 540px; height: 360px; padding: 44px 40px 0 50px;
    background: linear-gradient(180deg, #ffffff 0%, #f2f4f6 55%, #e4e8ec 100%); }
  .spread .backdrop { position: absolute; inset: 0; background: linear-gradient(160deg, transparent 40%, #dfe5ea 70%, #cfd7de 100%); }
  .spread .col-right > *:not(.backdrop) { position: relative; }
  .spread h3 { font-size: 15px; font-weight: 400; color: var(--orange); margin-bottom: 6px; }
  .spread .dates { list-style: none; margin: 0 0 18px 18px; }
  .spread .dates li { font-size: 12px; color: var(--orange); line-height: 1.55; }
  .spread .dates li b { font-weight: 400; display: inline-block; width: 76px; }
  .spread .dates li em { font-style: normal; font-size: 8.5px; color: var(--grey); margin-left: 4px; }
  .spread .programme { list-style: none; margin: 0 0 40px 18px; }
  .spread .programme li { font-size: 9px; line-height: 1.8; }
  .spread .programme li span { display: inline-block; width: 44px; }
  .spread .fee { font-size: 8.5px; line-height: 1.5; margin-bottom: 6px; }
  .spread .fee .lead { color: var(--orange); }

  /* ---------- cover ---------- */
  .cover { left: 115px; top: 620px; width: 370px; height: 560px; }
  .cover .peaks { position: absolute; left: 0; top: 0; width: 370px; height: 112px;
    background: linear-gradient(180deg, #ffffff 0%, #eef1f4 45%, #b7bfc7 70%, #f3f5f7 100%); }
  .cover .brand { position: absolute; right: 16px; top: 48px; font-size: 14px; }
  .cover .event { position: absolute; left: 16px; top: 140px; font-size: 16px; color: var(--orange); }
  .cover .event-dates { position: absolute; left: 16px; top: 168px; font-size: 10px; color: var(--grey); }
  .cover .event-dates span + span::before { content: "|"; color: var(--orange); margin: 0 6px; }
  .cover .bar { position: absolute; left: 0; top: 192px; width: 370px; height: 7px; background: var(--orange); }
  .cover .scene { position: absolute; left: 0; top: 199px; width: 370px; height: 361px;
    background: linear-gradient(180deg, var(--blue-deep) 0%, var(--blue) 28%, #8ea9c6 36%, #dfe6ec 44%, #eef2f5 70%, #d6dde4 100%); }
  .cover h1 { position: absolute; left: 16px; top: 212px; font-size: 26px; font-weight: 700; color: #fff; letter-spacing: 1px; }
  .cover h1 .akt { color: var(--orange); }
  .cover .subtitle { position: absolute; left: 16px; top: 248px; font-size: 14px; color: #fff; letter-spacing: .3px; }
  .cover .badge { position: absolute; right: 20px; bottom: 0; width: 142px; height: 36px; background: var(--orange);
    color: #fff; font-size: 14px; font-weight: 700; letter-spacing: .5px; display: flex; align-items: center; justify-content: center; }

  /* ---------- fax form ---------- */
  .fax { left: 525px; top: 620px; width: 560px; height: 560px; }
  .fax .blue-edge { position: absolute; right: 0; top: 150px; width: 22px; height: 410px; border-top-left-radius: 14px;
    background: linear-gradient(180deg, #1f5a94 0%, #3e78b0 45%, #cfd9e3 100%); }
  .fax h2 { position: absolute; left: 26px; top: 30px; font-size: 14px; font-weight: 400; color: var(--grey-dark); }
  .fax h2 .lead { color: var(--orange); }
  .fax .question { position: absolute; left: 26px; top: 92px; font-size: 8.5px; color: var(--orange); }
  .fax .options { position: absolute; left: 26px; top: 112px; font-size: 8.5px; color: var(--grey); line-height: 2.1; }
  .fax .options span { margin-right: 10px; }
  .fax .field-area { position: absolute; left: 0; top: 160px; width: 538px; height: 180px;
    background: linear-gradient(180deg, #f1f1f1 0%, #ffffff 40%); }
  .fax .fields { position: absolute; left: 26px; top: 180px; width: 240px; }
  .fax .row { display: flex; gap: 14px; height: 25.5px; border-bottom: 1px solid var(--line); align-items: flex-start; font-size: 6.5px; color: var(--orange); width: 240px; }
  .fax .row.wide { width: 240px; }
  .fax .row span:first-child { width: 56px; }
  .fax .row span.right { margin-left: auto; width: 86px; }
  .fax .notes { position: absolute; left: 26px; top: 396px; font-size: 6.5px; line-height: 1.6; color: var(--grey); }
  .fax .notes .lead { color: var(--orange); }
  .fax .organizer { position: absolute; left: 26px; top: 470px; font-size: 6.5px; line-height: 1.6; color: var(--grey); }
  .fax .organizer .lead { color: var(--orange); }
  .fax .brand { position: absolute; left: 270px; top: 470px; font-size: 11px; }
</style>
</head>
<body>

<!-- inner spread -->
<section class="sheet spread">
  <div class="photo-strip" role="img" aria-label="Fotoreihe: Bergsteiger mit Brille im Schnee, Kletterer an der Felswand und Seilschaft auf einem Gipfel"></div>
  <div class="strip-rule"></div>
  <div class="brand"><span class="dot"></span>Betriebs-Forum</div>

  <div class="col-left">
    <div class="title">BALANCE<span class="akt">AKT</span><small>Betriebs-Forum 2011</small></div>
    <div class="title-rule"></div>
    <p><span class="lead">Der Osttiroler Timo Konrad Brandler,</span> 44, ist von Geburt an blind. Seit seinem neunten Lebensjahr geht er seiner großen Leidenschaft, dem Klettern, nach und bewältigt auf diese Weise Touren im höchsten Schwierigkeitsgrad. Herzensprojekt ist es, als erster blinder Europäer die 7-Summits – die sieben höchsten Gipfel der Kontinente – zu erreichen. Schon sechs dieser legendären Bergriesen durfte er mit Händen und Füßen berühren.</p>
    <p><span class="lead">Den krönenden Abschluss</span> jedoch soll im Frühjahr 2012 die Besteigung des Mount Everest bilden. Zur Verwirklichung dieses Vorhabens braucht Timo Brandler starke Partner an seiner Seite. Denn im Leben – sind Erfolge ohne Zusammenhalt kaum möglich. Timo Brandler weiß, dass man sich auf andere verlassen muss, wenn man viel erleben kann.</p>
    <p>Mut, Ausdauer, Vertrauen, Teamgeist, Willenskraft, Professionalität und Leidenschaft – dafür steht er als Botschafter der österreichischen Betriebe. Helfen Sie mit, diesem einzigartigen Vorhaben zum Gipfel zu verhelfen: ein Vortrag über Forderung frei von Leistungsgrenzen.</p>
    <ul class="summits">
      <li>2008 Aconcagua, Südamerika – Kirgistan, Hochland</li>
      <li>2009 Kilimanjaro, Afrika – Denali, Alaska</li>
      <li>2010 Mt Vinson, Antarktis – Carstensz, Ozeanien</li>
    </ul>
  </div>

  <div class="col-right">
    <div class="backdrop" role="img" aria-label="Blasse Gletscherlandschaft im Hintergrund"></div>
    <h3>Termine</h3>
    <ul class="dates">
      <li><b>20.06.2011</b>GRAZ<em>Veranstaltungszentrum</em></li>
      <li><b>21.06.2011</b>WIEN<em>Veranstaltungszentrum</em></li>
      <li><b>30.06.2011</b>INNSBRUCK<em>Veranstaltungszentrum</em></li>
    </ul>
    <h3>Programm</h3>
    <ul class="programme">
      <li><span>16:00Uhr</span>Begrüßung</li>
      <li><span>16:15Uhr</span>Timo Brandler – „Blind auf die Gipfel der Welt“</li>
      <li><span>18:15Uhr</span>Get Together am Buffet</li>
    </ul>
    <p class="fee"><span class="lead">Teilnahmegebühr:</span> € 35,- pro Teilnehmer. Anmeldungen werden in der Reihenfolge des Eintreffens und nach Maßgabe freier Plätze berücksichtigt. Wir ersuchen Sie, nach Erhalt der Rechnung die Teilnahmegebühr umgehend zu überweisen.</p>
    <p class="fee"><span class="lead">Ermäßigung:</span> Bei Anmeldung &amp; Bezahlung über www.betriebs-forum.at verringert sich die Teilnahmegebühr auf € 30,-</p>
  </div>

  <div class="sponsors">
    <div class="sponsor"><span class="mark"></span>Nordwerk Autohaus</div>
    <div class="sponsor"><span class="mark wine"></span>www.vorsorge-partner.at</div>
    <div class="sponsor"><span class="mark navy"></span>Ing. Weber Lukas Wirtschaftsberatung</div>
  </div>
</section>

<!-- cover -->
<section class="sheet cover">
  <div class="peaks" role="img" aria-label="Verschneite Gebirgskette unter hellem Himmel"></div>
  <div class="brand"><span class="dot"></span>Betriebs-Forum GmbH</div>
  <div class="event">Betriebs-Forum 2011</div>
  <div class="event-dates"><span>20. Juni GRAZ</span><span>21. Juni WIEN</span><span>30. Juni INNSBRUCK</span></div>
  <div class="bar"></div>
  <div class="scene" role="img" aria-label="Gletscherlandschaft unter blauem Himmel mit Seilschaft und eingeblendeter Weltkarte der Seven Summits"></div>
  <h1>BALANCE<span class="akt">AKT</span></h1>
  <div class="subtitle">TIMO BRANDLER – blind climber</div>
  <div class="badge">EINLADUNG</div>
</section>

<!-- fax form -->
<section class="sheet fax">
  <div class="blue-edge" role="img" aria-label="Schmaler Bildstreifen mit blauem Himmel und Schnee"></div>
  <h2><span class="lead">Anmeldefax</span> +43 512 440217 16</h2>
  <div class="question">Ich nehme an folgender Veranstaltung teil:</div>
  <div class="options">
    <span>O 20.06. GRAZ</span><span>O 21.06. WIEN</span><span>O 30.06. INNSBRUCK</span><br>
    <span>O Ich werde in Begleitung kommen</span>
  </div>
  <div class="field-area"></div>
  <div class="fields">
    <div class="row"><span>Titel</span><span>Nachname</span><span class="right">Vorname</span></div>
    <div class="row"><span>Straße/Nr.</span><span class="right">PLZ/Ort</span></div>
    <div class="row wide"><span>Unternehmen</span></div>
    <div class="row wide"><span>E-Mail</span></div>
    <div class="row"><span>Telefon</span><span class="right">Fax</span></div>
    <div class="row wide"><span>&nbsp;</span></div>
    <div class="row"><span>Datum</span><span>Unterschrift</span></div>
  </div>
  <div class="notes">
    Aufgrund der begrenzten Teilnehmerzahl bitten wir<br>
    um verbindliche Anmeldung bis <span class="lead">Freitag, 17. Juni 2011</span>.<br>
    Telefon: +43 512 440217 | Fax: +43 512 440217 16<br>
    Mail: anmeldung@betriebs-forum.at | Web: www.betriebs-forum.at
  </div>
  <div class="organizer">
    <span class="lead">Veranstalter</span><br>
    Betriebs-Forum GmbH | Bergweg 12 | 6020 Innsbruck
  </div>
  <div class="brand"><span class="dot"></span>Betriebs-Forum</div>
</section>

</body>
</html>
```